Marlow Poise & Image Consultancy

Hi, I need a brochure design for my personal styling business. I have downloaded the company logo along with the content of the services offered for the brochure. Being a colour and styling business I would been keen on having some pictures of timeless fashion or colour samples, This is not absolutely necessary just an idea. I had also thought about changing and naming the services offered with a feminine, fun interesting type of theme. This may make it more inviting, I would be really interested in any of your creative ideas in this area. I will be deciding on the business card design in the next couple of days. I will download the design for this once I have made the decision. I will be okay to pay for any photo images that may be required if the brochure is selected. I had envisaged a tri fold brochure standard letter size with two folds (8.5" by 11inchs) however I am open to any suggestions. Please feel free to make any changes or modification's to the content, font etc in the files downloaded for the brochure. Many Thanks.
Updates
Project Deadline Extended
Reason: I need to extend the time for this project as I do not have all of content required for the brochure confirmed. Many Thanks
Industry/Entity Type
Fashion
Font styles to use
Look and feel
Each slider illustrates characteristics of the customer's brand and the style your logo design should communicate.

```html
<!DOCTYPE html>
<html lang="en">
<head>
<meta charset="utf-8">
<title>Marlow Poise &amp; Image Consultancy – Brochure</title>
<link rel="stylesheet" href="https://fonts.googleapis.com/css2?family=Cherry+Swash&family=Lato:wght@300;400;700&family=Open+Sans:wght@700&display=swap">
<style>
:root{
  --ink:#141414;
  --panel-dark:#1c1c1c;
  --gold-light:#c9a543;
  --gold:#b08d2f;
  --gold-deep:#8f7124;
  --pink:#e0207a;
  --orange:#f0a232;
  --white:#ffffff;
  --grey:#5a5a5a;
  --grey-light:#8a8a8a;
}
*{box-sizing:border-box;margin:0;padding:0}
html,body{width:1200px;height:927px;overflow:hidden;background:#fff}
.brochure{position:relative;width:1200px;height:927px;overflow:hidden;font-family:'Lato',sans-serif}

/* Left panel */
.panel-intro{position:absolute;left:0;top:0;width:404px;height:927px;
  background:linear-gradient(180deg,var(--gold) 40%,var(--gold-light) 65%,var(--gold-deep) 100%)}
.photo-portrait{position:absolute;left:0;top:0;width:404px;height:460px;
  background:linear-gradient(160deg,#e8c98e 0%,#b98a52 40%,#6b4a2c 75%,#3a2a1e 100%)}
.intro-wave{position:absolute;left:0;top:395px;width:404px;height:80px}
.intro-copy{position:absolute;left:31px;top:500px;width:345px;color:var(--white);
  font-weight:300;font-size:14.6px;line-height:22.4px;text-align:justify}
.intro-copy p+p{margin-top:22px}

/* Middle panel */
.panel-services{position:absolute;left:404px;top:0;width:396px;height:927px;background:var(--ink)}
.services-title{position:absolute;left:26px;top:14px;font-family:'Cherry Swash',cursive;
  font-weight:400;font-size:28px;color:var(--orange);letter-spacing:.3px}
.services-list{position:absolute;left:25px;top:62px;width:349px;color:var(--white);
  font-size:11.3px;line-height:13.3px;text-align:justify;font-weight:400}
.services-list h3{color:var(--pink);font-size:11.3px;font-weight:700;line-height:13.3px;margin-top:4px}
.services-list h3:first-child{margin-top:0}
.contact-heading{position:absolute;left:48px;top:795px;font-family:'Open Sans',sans-serif;
  font-weight:700;font-size:47px;color:var(--grey);letter-spacing:-.5px}

/* Right panel */
.panel-cover{position:absolute;left:800px;top:0;width:400px;height:927px;background:var(--panel-dark)}
.photo-beach{position:absolute;left:0;top:0;width:400px;height:460px;
  background:linear-gradient(180deg,#dfeeee 0%,#b9dcd9 35%,#4fa7a7 60%,#2d8588 80%,#4c8a80 100%)}
.cover-wave{position:absolute;left:0;top:400px;width:400px;height:80px}
.cover-headline{position:absolute;left:0;top:480px;width:400px;text-align:center;
  font-family:'Cherry Swash',cursive;font-weight:400;font-size:52px;line-height:57px;color:var(--white)}
.cover-headline .accent{color:var(--orange);display:block;font-size:56px;line-height:66px}
.brand{position:absolute;left:40px;top:755px;width:330px;display:flex;align-items:center;gap:14px}
.brand-dot{width:34px;height:34px;border-radius:50%;background:var(--grey-light);flex:none}
.brand-name{font-family:'Lato',sans-serif;font-weight:700;font-size:23px;line-height:27px;color:var(--grey-light)}
</style>
</head>
<body>
<main class="brochure">

  <section class="panel-intro">
    <div class="photo-portrait" role="img" aria-label="Fashion photo of a woman in sunglasses and a camel coat on a city street"></div>
    <svg class="intro-wave" viewBox="0 0 404 80" preserveAspectRatio="none" aria-hidden="true">
      <path d="M0 30 C120 -5 260 -5 404 10 L404 80 L0 80 Z" fill="#6e6e6e"/>
      <path d="M0 40 C120 5 260 5 404 20 L404 80 L0 80 Z" fill="#111"/>
      <path d="M0 52 C120 18 260 18 404 32 L404 80 L0 80 Z" fill="var(--gold)"/>
    </svg>
    <div class="intro-copy">
      <p>Time for a change, take a fresh look and discover how to dress in a style that reflects your personality &amp; lifestyle. Be confident, look amazing &amp; feel great about the way that you look every day. Some people always look effortlessly stylish, looking good is all about knowing what suits you.</p>
      <p>As a personal stylist I am committed to creating a fabulous style that works for you. I take time to engage with my clients, learn about your lifestyle and work through a process to establish your signature style. Be empowered and understand how you can dress for success everyday. Discover the elements in creating an overall balance and harmony in putting together a stylish functional wardrobe that reflects you and your lifestyle.</p>
    </div>
  </section>

  <section class="panel-services">
    <h2 class="services-title">Personal Styling Services</h2>
    <div class="services-list">
      <h3>Ultimate Party Experience</h3>
      <p>Get a group of women together open the bubbly, enjoy some nibbles and prepare yourselves for a fun and informative time when you book one of our party packages. We can tailor a party experience for any occasion. Great for birthdays, hen's party, ladies night out! We can travel to your home or required location.<br>Style Party Package<br>We initially present to you as a group discuss valuable styling tips, it's amazing the difference it can make just by altering a garment by a few centimetres or knowing how to pull an outfit all together with accessories. We then spend time one on one and everyone will learn about their unique style personality, understand their body shape and will be provided with valuable styling tips suited for them. Each person will receive a style notebook with personalised notes to take away.<br>Duration: From 2 hours up to 4 hours depending.<br>Price: From $65.00 to $85.00 per person<br>Note prices may vary depending on numbers, specific requests, location.</p>
      <h3>Colour Party Package</h3>
      <p>We initially present to you as a group, discussing colour and how we can use colour to enhance our appearance and balance our silhouette. We also discuss style tips on pulling an outfit together using colour &amp; accessories. We will then spend time one on one with each person to discuss their dominant colouring and what that means to the clothes and make up they wear. Everyone will learn how to wear colour to best suit their personality and body shape. If clients would like they may purchase a colour swatch with their perfect colours $89.00 each.<br>Duration: From 2 to 4 hours depending<br>Price: From $65.00 to $85.00 per person plus travel costs<br>Note prices may vary depending on numbers, specific requests, location.</p>
      <h3>Make up Party Package</h3>
      <p>A makeup party is a great way to get together with some friends and learn some new makeup tips to keep your look current and stylish, we discuss the latest trends and techquies and how to wear them to compliment your look. We can arrange and tailor a make-up party for any occasion. Inquire to discuss ideas to make your next occasion a fun &amp; memorable experience.<br>Price From $25.00 to $45.00 per person Depending on specific requests and numbers.</p>
      <h3>All Party Packages include:</h3>
      <p>Complimentary Food Platter<br>Complimentary glass of bubbles or orange juice per person<br>Note: Prices may vary on all party packages, depending upon various factors like specific requests, travel costs, location and the experience offered for the occasion.</p>
    </div>
    <p class="contact-heading">contact info</p>
  </section>

  <section class="panel-cover">
    <div class="photo-beach" role="img" aria-label="Fashion photo of a woman in a lace dress and sun hat standing in the sea"></div>
    <svg class="cover-wave" viewBox="0 0 400 80" preserveAspectRatio="none" aria-hidden="true">
      <path d="M0 55 C110 20 260 0 400 12 L400 80 L0 80 Z" fill="var(--gold)"/>
      <path d="M0 64 C110 30 260 12 400 24 L400 80 L0 80 Z" fill="var(--panel-dark)"/>
    </svg>
    <h1 class="cover-headline">Dress For<br>The Life You<span class="accent">Love</span></h1>
    <div class="brand">
      <span class="brand-dot" aria-hidden="true"></span>
      <span class="brand-name">Marlow Poise &amp; Image Consultancy</span>
    </div>
  </section>

</main>
</body>
</html>
```